Letterhead Design

We need a new Letterhead design for a 30 year old Electrical Company. We service domestic and commercial places. We have a logo recently made so to incorporate that. Using same colours or interested to see others added.
Would like to see a couple of options with all the info in letterhead, then another with info in a footnote down the bottom.

info needed to be added:

-Lic. No 48120
3/22-24 Tallow Rd, Banksmeadow 2019
W - dorrickpower.com.au
T - (02) 9483 1720
M - 0437 592 816
E - info@dorrickpower.com.au
ABN: 41 729 504 316

```html
<!DOCTYPE html>
<html lang="en">
<head>
<meta charset="utf-8">
<title>Dorrick Power – Letterhead and Folder</title>
<link rel="stylesheet" href="https://fonts.googleapis.com/css2?family=Crimson+Text:wght@400;600&family=Questrial&display=swap">
<style>
  :root {
    --backdrop: #e3e7e9;
    --backdrop-edge: #d4d9dc;
    --paper: #ffffff;
    --ink: #2b2b2b;
    --ink-soft: #3a3a3a;
    --brand-dark: #263433;
    --orange: #f7941d;
    --orange-light: #ffa31f;
    --orange-deep: #ff8712;
    --band-dark: #2a2a2a;
    --faint: #dadada;
  }
  * { margin: 0; padding: 0; box-sizing: border-box; }
  html, body { width: 1200px; height: 784px; overflow: hidden; }
  body {
    position: relative;
    background: radial-gradient(ellipse at 50% 40%, var(--backdrop) 55%, var(--backdrop-edge) 100%);
    font-family: "Questrial", "Century Gothic", sans-serif;
    color: var(--ink);
  }

  .letterhead {
    position: absolute; left: 42px; top: 44px; width: 513px; height: 698px;
    background: var(--paper); border-radius: 14px; overflow: hidden;
    box-shadow: 0 2px 6px rgba(0,0,0,.18);
  }
  .header-name, .faint-name, .folder-name {
    position: absolute;
    font-family: "Crimson Text", Georgia, serif; font-weight: 600;
    white-space: nowrap; line-height: 1;
  }
  .header-name {
    top: 24px; left: 0; width: 100%; text-align: center;
    font-size: 28px; color: var(--brand-dark);
  }
  .contact-row {
    position: absolute; top: 96px; left: 0; width: 100%;
    display: flex; justify-content: center; gap: 14px;
    font-family: "Crimson Text", Georgia, serif; font-size: 9.5px; color: var(--ink-soft);
  }
  .contact-item { display: flex; align-items: center; gap: 4px; }
  .contact-item svg { width: 9px; height: 9px; fill: var(--orange); }
  .address {
    position: absolute; top: 111px; left: 0; width: 100%; text-align: center;
    font-family: "Crimson Text", Georgia, serif; font-weight: 600;
    font-size: 8px; color: var(--orange);
  }
  .letter-body {
    position: absolute; top: 146px; left: 48px; width: 425px;
    font-size: 11.2px; line-height: 18px; text-align: justify; color: var(--ink-soft);
    hyphens: auto;
  }
  .letter-body p + p { margin-top: 16px; }
  .faint-name {
    left: 48px; top: 568px;
    font-size: 24px; color: var(--faint);
  }
  .signature { position: absolute; left: 384px; top: 587px; }
  .signature .name { font-size: 14px; color: var(--ink); }
  .signature .role { font-size: 9px; margin-top: 6px; color: var(--ink-soft); }
  .footer-wave { position: absolute; left: 0; top: 620px; width: 513px; height: 78px; }
  .footer-info {
    position: absolute; left: 48px; top: 650px;
    font-family: "Crimson Text", Georgia, serif; font-weight: 600;
    font-size: 8px; line-height: 12px; color: #fff;
  }
  .footer-info .abn { color: var(--orange); }
  .footer-info .web { letter-spacing: 1.4px; }

  .folder {
    position: absolute; left: 634px; top: 44px; width: 513px; height: 698px;
    background: linear-gradient(160deg, var(--orange-light) 0%, var(--orange) 55%, var(--orange-deep) 100%);
    border-radius: 14px; overflow: hidden;
    box-shadow: 0 2px 6px rgba(0,0,0,.18);
  }
  .folder-tab { position: absolute; right: 0; top: 150px; width: 40px; height: 220px; }
  .folder-name {
    left: 123px; top: 514px;
    font-size: 38px; color: #2d2a27;
  }
</style>
</head>
<body>
  <section class="letterhead">
    <div class="header-name">Dorrick Power</div>

    <div class="contact-row">
      <span class="contact-item">
        <svg viewBox="0 0 10 10"><path d="M1 7.5C1 5 3 3.5 5 3.5S9 5 9 7.5V9H1Z M0 3C1.5 1 8.5 1 10 3L9 4.5 7 4 7 3C6 2.6 4 2.6 3 3L3 4 1 4.5Z"/></svg>
        (02) 9483 1720
      </span>
      <span class="contact-item">
        <svg viewBox="0 0 10 10"><path d="M3 0H7A1 1 0 0 1 8 1V9A1 1 0 0 1 7 10H3A1 1 0 0 1 2 9V1A1 1 0 0 1 3 0ZM3 1.5V8H7V1.5Z"/></svg>
        0437 592 816
      </span>
      <span class="contact-item">
        <svg viewBox="0 0 10 10"><path d="M0 2H10V8H0ZM0.8 2.6 5 5.6 9.2 2.6V2.2H0.8Z"/></svg>
        info@dorrickpower.com.au
      </span>
    </div>
    <div class="address">3/22-24 Tallow Rd, Banksmeadow 2019</div>

    <div class="letter-body">
      <p>Lorem ipsum dolor sit amet, consectetur adipiscing elit. Donec orci purus, luctus vitae dignissim eu, iaculis sed purus. Vivamus faucibus, ipsum nec aliquet viverra, leo mauris condimentum ligula, sit amet sagittis enim ligula quis arcu. Nam egestas tortor id nisi porttitor mattis. In tortor ante, ultricies in suscipit a, tempus non massa. Vivamus et auctor mi. Fusce vel massa nulla. Phasellus nec eros mauris, et scelerisque orci. Donec malesuada orci vitae nulla accumsan porta a id massa.</p>
      <p>Quisque accumsan iaculis magna sit amet fringilla. Maecenas consequat, magna eget tincidunt semper, odio nibh rutrum mi, id feugiat ante nisi eu risus. Vestibulum nunc orci, rhoncus a placerat in, ultricies in mi. Cras mattis varius eros, vel fringilla nisi suscipit eget. Quisque scelerisque sagittis nulla at porttitor. Mauris a justo et tellus interdum tristique. Sed id augue vitae urna euismod commodo aliquet a quam. Pellentesque arcu velit, cursus et malesuada ut, consequat et diam. Nullam erat sem, rhoncus id ullamcorper vitae, rhoncus et arcu. In ultricies ultricies nulla,</p>
      <p>Kut rutrum nisi iaculis at. Donec eu magna a metus ornare faucibus. Fusce aliquet faucibus ultricies. Morbi semper, est id tincidunt gravida, sem arcu adipiscing lacus, ac bibendum nulla leo eu purus. Quisque nec diam sed risus consectetur a ccumsan quis quis nibh. Vestibulum id purus lorem. Donec eu magna a metus ornare faucibus. Fusce aliquet faucibus ultricies. Morbi semper, est id tincidunt gravida, sem arcu adipiscing lacus, ac bibendum nulla leo eu purus. Quisque nec diam sed risus consectetur a ccumsan quis quis nibh. Vestibulum id purus lorem.</p>
    </div>

    <div class="faint-name">Dorrick Power</div>

    <div class="signature">
      <div class="name">Owen Tallis</div>
      <div class="role">Co-Founder &amp; CEO</div>
    </div>

    <svg class="footer-wave" viewBox="0 0 513 78" preserveAspectRatio="none" aria-hidden="true">
      <path fill="var(--orange)" d="M0 10 C120 -4 250 8 360 34 C430 50 480 46 513 34 L513 78 L0 78Z"/>
      <path fill="var(--band-dark)" d="M0 20 C130 10 260 26 360 52 C430 70 480 66 513 56 L513 78 L0 78Z"/>
    </svg>

    <div class="footer-info">
      <div class="lic">Lic. No 48120</div>
      <div class="abn">ABN: 41 729 504 316</div>
      <div class="web">www.dorrickpower.com.au</div>
    </div>
  </section>

  <section class="folder">
    <svg class="folder-tab" viewBox="0 0 40 220" preserveAspectRatio="none" aria-hidden="true">
      <path fill="rgba(230,110,10,0.35)" d="M40 0 C20 6 4 12 4 30 L4 220 L40 220Z"/>
    </svg>
    <div class="folder-name">Dorrick Power</div>
  </section>
</body>
</html>
```